Complete Stationary Package Needed for New Dental Office ! ! !

I'm moving my dental office and would like to use my existing logo to create a new:
- Business Card (please submit Business Card designs to this project - http://tasks.artbidhub.example/task.aspx?id=514290)
- Appointment Card (submit here)
- Letterhead (submit here)
- Envelope (submit here)
My practice name (within my logo) is:
Melvin R. Tuttle, D.D.S., P.A.
Family and Cosmetic Dentistry
***Obviously you will notice that the lower leg of the "T" in my logo is a smile.
My new address and contact information is:
340 Larkspur Commons Drive, Suite 118
Cary, NC 27593
919-472-3081 (ph)
919-472-3095 (fax)
info@tuttledds.example
www.tuttledds.example
If you would like to use a tagline, I would suggest "Precision Dentistry with a Personal Touch".
I have attached my logo in numerous formats.
I have also attached 2 QR codes, one of which links to my website and the other one which links to a "Like" page for my business Chatterly page. These QR codes could be improved by putting a graphic in the middle, but I created these myself and did not know how to do this.
Thank you for your time. I look forward to seeing all of your creative ideas!
Depending on the designs, I may award 2 different winners for the Business Card project and the Stationery Project. Or if a design is really good, I will award both projects to the same designer.
Updates
Project Deadline Extended
Reason: PixelBazaar administrators recently helped me split my project into 2 projects - 1 for business card and 1 for letterhead, envelope, etc. and I would like sufficient time to receive designs and provide feedback. Thank you.
Target Market(s)
Current and prospective dental patients.
Industry/Entity Type
Dental
Requirements
Must have
- Please ensure business card has a 2-sided design.
- Please ensure that your design is "practical" for printing purposes.
Nice to have
- Improvement of QR codes by addition of graphics in the middle to differentiate them. Incorporation of QR codes into business card design, maybe on the back side? I would consider the Chatterly QR code more important than the website QR code simply because my website URL is very easy to type.
Should not have
- Please, NO "floating" or "extracted" teeth which sends an undesirable message.

```html
<!DOCTYPE html>
<html lang="en">
<head>
<meta charset="utf-8">
<title>Melvin R. Tuttle, D.D.S., P.A. — Stationery</title>
<link rel="stylesheet" href="https://fonts.googleapis.com/css2?family=Cinzel:wght@400;600&family=Cormorant+Garamond:ital,wght@0,500;1,500&display=swap">
<style>
:root{
  --backdrop:#e8e9eb;
  --paper:#ffffff;
  --navy:#1f2c78;
  --navy-deep:#18205e;
  --teal:#2fb1a4;
  --ink:#4a4d57;
  --ink-soft:#8a8d96;
}
*{box-sizing:border-box;margin:0;padding:0}
html,body{width:1200px;height:800px;overflow:hidden}
body{background:var(--backdrop);position:relative;font-family:"Cormorant Garamond",Georgia,serif;color:var(--ink)}
.sheet{position:absolute;background:var(--paper);box-shadow:0 6px 18px rgba(0,0,0,.12)}
.brand{display:flex;align-items:center;gap:7px}
.brand-mark{width:26px;height:26px;background:var(--navy);flex:none}
.brand-name{font-family:"Cinzel",Georgia,serif;font-weight:600;color:var(--navy);font-size:13px;letter-spacing:.5px;line-height:1;white-space:nowrap}
.brand-sub{font-family:"Cinzel",Georgia,serif;color:var(--teal);font-size:8px;letter-spacing:.6px;margin-top:3px;white-space:nowrap}

/* Letterhead */
.letterhead{left:650px;top:80px;width:480px;height:640px}
.letterhead .brand{position:absolute;right:40px;top:38px}
.header-band{position:absolute;right:0;top:104px;width:240px;height:92px}
.header-band svg{position:absolute;inset:0}
.header-contacts{position:absolute;right:14px;top:124px;width:190px;display:grid;grid-template-columns:1fr 1fr;gap:12px 8px;color:#fff;font-size:7px;line-height:1.3}
.contact{display:flex;gap:4px;align-items:flex-start}
.contact svg{flex:none;width:9px;height:9px}
.letter-body{position:absolute;left:46px;top:210px;width:330px;font-size:9.5px;line-height:1.45;text-transform:uppercase;letter-spacing:.2px;text-align:justify}
.letter-body p{margin-bottom:10px}
.letter-body .sign{text-align:left}
.footer-band{position:absolute;left:0;bottom:36px;width:320px;height:48px}
.footer-band svg{position:absolute;inset:0}
.tagline{position:absolute;left:16px;bottom:55px;color:#fff;font-style:italic;font-size:9px;letter-spacing:.5px;text-transform:uppercase;white-space:nowrap}

/* Business cards */
.card{width:380px;height:217px;overflow:hidden}
.card-front{left:90px;top:150px}
.card-back{left:130px;top:440px}
.card-front .brand{position:absolute;left:22px;top:26px;align-items:flex-start}
.card-front .brand-name{font-size:9.5px;white-space:normal;width:150px;line-height:1.2}
.card-front .brand-sub{font-size:6.5px}
.card-person{position:absolute;left:22px;top:82px;font-family:"Cinzel",Georgia,serif;color:var(--navy);font-size:10px;letter-spacing:.4px}
.card-contacts{position:absolute;left:218px;top:28px;width:150px;display:flex;flex-direction:column;gap:7px;font-size:8px;line-height:1.25;color:var(--ink)}
.card-contacts svg{width:9px;height:9px;flex:none}
.card-corner{position:absolute;right:0;bottom:0;width:200px;height:70px}
.card-back .brand{position:absolute;left:50%;top:72px;transform:translateX(-50%)}
.card-back .brand-name{font-size:14px}
.card-web{position:absolute;left:0;right:0;top:130px;text-align:center;font-size:9px;color:var(--ink-soft);letter-spacing:.4px}
.card-base{position:absolute;left:0;bottom:0;width:380px;height:40px}
</style>
</head>
<body>

<section class="sheet letterhead" aria-label="Letterhead">
  <div class="brand">
    <span class="brand-mark"></span>
    <div>
      <div class="brand-name">Melvin R. Tuttle, D.D.S., P.A.</div>
      <div class="brand-sub">Family and Cosmetic Dentistry</div>
    </div>
  </div>

  <div class="header-band">
    <svg viewBox="0 0 240 92" preserveAspectRatio="none">
      <path d="M22 0 H240 V92 H4 C14 70 6 30 22 0Z" fill="var(--teal)"/>
      <path d="M32 0 H240 V92 H14 C24 70 16 30 32 0Z" fill="var(--navy)"/>
    </svg>
  </div>
  <div class="header-contacts">
    <div class="contact"><svg viewBox="0 0 10 10"><path d="M2 1 L4 1 L5 3 L4 4 C4.6 5.4 5 5.8 6 6 L7 5 L9 6 L9 8 C6 9.5 0.5 4 2 1Z" fill="#fff"/></svg><span>919-472-3081<br>919-472-3095</span></div>
    <div class="contact"><svg viewBox="0 0 10 10"><path d="M5 0.5 C7 0.5 8.3 2 8.3 3.8 C8.3 6 5 9.5 5 9.5 C5 9.5 1.7 6 1.7 3.8 C1.7 2 3 0.5 5 0.5Z" fill="#fff"/><circle cx="5" cy="3.8" r="1.2" fill="var(--navy)"/></svg><span>340 Larkspur Commons Drive, Suite 118<br>Cary, NC 27593</span></div>
    <div class="contact"><svg viewBox="0 0 10 10"><rect x="0.5" y="2" width="9" height="6" fill="#fff"/><path d="M0.5 2 L5 5.5 L9.5 2" stroke="var(--navy)" stroke-width="0.8" fill="none"/></svg><span>info@tuttledds.example</span></div>
    <div class="contact"><svg viewBox="0 0 10 10"><circle cx="5" cy="5" r="4.3" fill="none" stroke="#fff" stroke-width="0.9"/><path d="M0.7 5 H9.3 M5 0.7 C2.5 3 2.5 7 5 9.3 M5 0.7 C7.5 3 7.5 7 5 9.3" stroke="#fff" stroke-width="0.7" fill="none"/></svg><span>www.tuttledds.example</span></div>
  </div>

  <div class="letter-body">
    <p>Dear Sir/Madam,</p>
    <p>Thank you for choosing our practice for your family's dental care. We are pleased to welcome you to our new office and look forward to meeting you soon.</p>
    <p>Our team offers gentle cleanings, fillings, crowns and whitening in a calm and modern setting designed around your comfort.</p>
    <p>Please arrive ten minutes before your visit and bring your insurance card and a list of current medications.</p>
    <p>If you have any questions, call our front desk at any time during office hours.</p>
    <p class="sign">Yours faithfully,</p>
    <p class="sign">Melvin R. Tuttle</p>
  </div>

  <div class="footer-band">
    <svg viewBox="0 0 320 48" preserveAspectRatio="none">
      <path d="M0 0 H282 C306 0 300 48 320 48 H0Z" fill="var(--teal)"/>
      <path d="M0 0 H272 C296 0 290 48 310 48 H0Z" fill="var(--navy)"/>
    </svg>
  </div>
  <div class="tagline">"Precision Dentistry with a Personal Touch"</div>
</section>

<section class="sheet card card-front" aria-label="Business card front">
  <div class="brand">
    <span class="brand-mark"></span>
    <div>
      <div class="brand-name">Melvin R. Tuttle, D.D.S., P.A.</div>
      <div class="brand-sub">Family and Cosmetic Dentistry</div>
    </div>
  </div>
  <div class="card-person">Melvin R. Tuttle</div>
  <div class="card-contacts">
    <div class="contact"><svg viewBox="0 0 10 10"><path d="M5 0.5 C7 0.5 8.3 2 8.3 3.8 C8.3 6 5 9.5 5 9.5 C5 9.5 1.7 6 1.7 3.8 C1.7 2 3 0.5 5 0.5Z" fill="var(--navy)"/></svg><span>340 Larkspur Commons Drive, Suite 118<br>Cary, NC 27593</span></div>
    <div class="contact"><svg viewBox="0 0 10 10"><path d="M2 1 L4 1 L5 3 L4 4 C4.6 5.4 5 5.8 6 6 L7 5 L9 6 L9 8 C6 9.5 0.5 4 2 1Z" fill="var(--navy)"/></svg><span>919-472-3081</span></div>
    <div class="contact"><svg viewBox="0 0 10 10"><rect x="1" y="1" width="8" height="8" fill="none" stroke="var(--navy)"/></svg><span>919-472-3095</span></div>
    <div class="contact"><svg viewBox="0 0 10 10"><rect x="0.5" y="2" width="9" height="6" fill="var(--navy)"/></svg><span>info@tuttledds.example</span></div>
  </div>
  <svg class="card-corner" viewBox="0 0 200 70" preserveAspectRatio="none">
    <path d="M0 70 C60 70 70 20 120 8 L200 0 V70Z" fill="var(--teal)"/>
    <path d="M14 70 C70 70 80 28 130 16 L200 8 V70Z" fill="var(--navy)"/>
  </svg>
</section>

<section class="sheet card card-back" aria-label="Business card back">
  <div class="brand">
    <span class="brand-mark"></span>
    <div>
      <div class="brand-name">Melvin R. Tuttle, D.D.S., P.A.</div>
      <div class="brand-sub">Family and Cosmetic Dentistry</div>
    </div>
  </div>
  <div class="card-web">www.tuttledds.example</div>
  <svg class="card-base" viewBox="0 0 380 40" preserveAspectRatio="none">
    <path d="M0 0 H160 C190 0 190 40 220 40 H0Z" fill="var(--teal)"/>
    <path d="M0 6 H150 C178 6 180 40 208 40 H0Z" fill="var(--navy)"/>
  </svg>
</section>

</body>
</html>
```